Networking card

I just need a simple design with the following information:
Ravin Doshu
318.647.2094
rdoshu583016@mailvanta.com

I would like to have a white background with blue text like in this sample: https://cardmintly.com/business-card-207346/

```html
<!DOCTYPE html>
<html lang="en">
<head>
<meta charset="utf-8">
<title>Ravin Doshu – Networking Card</title>
<link href="https://fonts.googleapis.com/css2?family=Montserrat:wght@400;500;700&display=swap" rel="stylesheet">
<style>
  :root {
    --navy: #0c365c;
    --white: #ffffff;
    --backdrop: #c9cacd;
    --card-shadow: rgba(0, 0, 0, 0.22);
  }
  * { box-sizing: border-box; margin: 0; padding: 0; }
  html, body {
    width: 1200px;
    height: 939px;
    overflow: hidden;
  }
  body {
    background: var(--backdrop);
    font-family: "Montserrat", sans-serif;
    position: relative;
  }
  .card {
    position: absolute;
    width: 560px;
    height: 320px;
    box-shadow: 0 6px 18px var(--card-shadow);
  }
  .card--front {
    left: 90px;
    top: 110px;
    background: var(--navy);
    color: var(--white);
    display: flex;
    flex-direction: column;
    align-items: center;
    justify-content: center;
    gap: 22px;
  }
  .card--back {
    left: 550px;
    top: 510px;
    background: var(--white);
    color: var(--navy);
  }
  .brand-dot {
    width: 84px;
    height: 84px;
    border-radius: 50%;
    border: 5px solid currentColor;
  }
  .brand-name {
    font-weight: 500;
    font-size: 30px;
    letter-spacing: 1.5px;
    text-transform: uppercase;
  }
  .card--back .brand {
    position: absolute;
    right: 44px;
    top: 58px;
    display: flex;
    flex-direction: column;
    align-items: center;
    gap: 16px;
  }
  .card--back .brand-dot {
    width: 64px;
    height: 64px;
    border-width: 4px;
  }
  .card--back .brand-name { font-size: 22px; }
  .holder {
    position: absolute;
    left: 44px;
    top: 150px;
  }
  .holder-name {
    font-size: 22px;
    text-transform: uppercase;
    letter-spacing: 0.5px;
  }
  .holder-name strong { font-weight: 700; }
  .holder-name span { font-weight: 400; }
  .holder-role {
    font-size: 11px;
    font-weight: 500;
    margin-left: 12px;
    margin-top: 2px;
  }
  .contact-list {
    list-style: none;
    margin-top: 22px;
    margin-left: 12px;
    display: flex;
    flex-direction: column;
    gap: 8px;
  }
  .contact-item {
    display: flex;
    align-items: center;
    gap: 10px;
    font-size: 14px;
  }
  .contact-item--phone { letter-spacing: 3px; font-size: 15px; }
  .contact-icon {
    width: 24px;
    height: 24px;
    background: var(--navy);
    display: flex;
    align-items: center;
    justify-content: center;
    flex: none;
  }
  .contact-icon svg { width: 14px; height: 14px; fill: none; stroke: var(--white); stroke-width: 2; }
</style>
</head>
<body>
  <section class="card card--front" aria-label="Card front">
    <div class="brand-dot" aria-hidden="true"></div>
    <div class="brand-name">Ravin Doshu</div>
  </section>

  <section class="card card--back" aria-label="Card back">
    <div class="holder">
      <div class="holder-name"><strong>Ravin</strong> <span>Doshu</span></div>
      <div class="holder-role">President</div>
      <ul class="contact-list">
        <li class="contact-item contact-item--phone">
          <span class="contact-icon">
            <svg viewBox="0 0 24 24"><path d="M5 3h4l2 5-3 2a11 11 0 0 0 6 6l2-3 5 2v4a2 2 0 0 1-2 2A18 18 0 0 1 3 5a2 2 0 0 1 2-2z" fill="#fff" stroke="none"/></svg>
          </span>
          318.647.2094
        </li>
        <li class="contact-item">
          <span class="contact-icon">
            <svg viewBox="0 0 24 24"><rect x="3" y="6" width="18" height="12"/><path d="M3 6l9 7 9-7M3 18l7-6M21 18l-7-6"/></svg>
          </span>
          rdoshu583016@mailvanta.com
        </li>
      </ul>
    </div>
    <div class="brand">
      <div class="brand-dot" aria-hidden="true"></div>
      <div class="brand-name">Ravin Doshu</div>
    </div>
  </section>
</body>
</html>
```